Brisco Skiff Ferry and Haulage Business Card

I need business cards for my new water taxi and freight transport business I have started here in Kodiak Alaska. Kodiak is a remote island in the middle of the gulf of Alaska. There are seven native villages around the island and Kodiak is the #2 fishing port in the United States. We also have the largest Harbor Watch Base in the U.S. My company will be providing water taxi and freight transport logistics to the villages and many hunting and fishing lodges as well as remote properties around the island.

I would like a business card that isn't status quo, something that stands out, either in feel or appearance. I do like clean minimal designs but it needs to have the necessary contact info on it.

Target Market(s)

remote lodge / property owners, residents of the many villages around Kodiak and any one wanting to enjoy the great outdoors of Kodiak Alaska

Industry/Entity Type

Business

Contact Information for Business Card

I like clean simple designs that aren't cluttered but still provide the necessary information

Colors
0255a3
3277b5
33a4d5
9bcb3c
add136
fbed22
ffc214
f78f20
f37122

Requirements
Must have
• logo and contact info
• Captain Wade Pemberton
• www.briscoskiffferry.net
• wade@briscoskiffferry.net

```html
<!DOCTYPE html>
<html lang="en">
<head>
<meta charset="utf-8">
<title>Brisco Skiff Ferry and Haulage – Business Card</title>
<link href="https://fonts.googleapis.com/css2?family=Quicksand:wght@400;700&display=swap" rel="stylesheet">
<style>
  :root {
    --page-bg: #ffffff;
    --card-white: #ffffff;
    --card-orange: #f37122;
    --brand-blue: #0255a3;
    --ink: #1d1d1d;
    --light-ink: #ffffff;
    --edge: #9a9a9a;
  }
  html, body {
    margin: 0;
    padding: 0;
    width: 1200px;
    height: 1000px;
    overflow: hidden;
    background: var(--page-bg);
  }
  .canvas {
    position: relative;
    width: 1200px;
    height: 1000px;
  }
  .business-card {
    position: absolute;
    left: 195px;
    top: 247px;
    width: 795px;
    height: 401px;
    background: var(--card-orange);
    outline: 1px solid var(--edge);
    overflow: hidden;
    font-family: "Quicksand", sans-serif;
  }
  .card-sweep {
    position: absolute;
    inset: 0;
  }
  .card-sweep path { fill: var(--card-white); }
  .captain-name {
    position: absolute;
    left: 20px;
    top: 10px;
    margin: 0;
    font-size: 25px;
    font-weight: 400;
    color: var(--light-ink);
    letter-spacing: 0.2px;
  }
  .brand-name {
    position: absolute;
    left: 190px;
    top: 180px;
    width: 460px;
    margin: 0;
    text-align: center;
    font-weight: 700;
    color: var(--brand-blue);
    line-height: 1;
  }
  .brand-name .brand-main {
    display: block;
    font-size: 64px;
    letter-spacing: 1px;
  }
  .brand-name .brand-sub {
    display: block;
    margin-top: 6px;
    font-size: 30px;
  }
  .contact {
    position: absolute;
    bottom: 10px;
    margin: 0;
    font-size: 21px;
    font-weight: 400;
    color: var(--ink);
  }
  .contact-email { left: 20px; }
  .contact-web { right: 20px; }
</style>
</head>
<body>
<div class="canvas">
  <section class="business-card">
    <svg class="card-sweep" width="795" height="401" viewBox="0 0 795 401" aria-hidden="true">
      <path d="M358,0 L795,0 L795,401 L655,401 C520,380 420,300 385,170 C368,110 360,55 358,0 Z"/>
    </svg>
    <h1 class="captain-name">Captain Wade Pemberton</h1>
    <p class="brand-name">
      <span class="brand-main">Brisco Skiff</span>
      <span class="brand-sub">Ferry and Haulage</span>
    </p>
    <p class="contact contact-email">wade@briscoskiffferry.net</p>
    <p class="contact contact-web">www.briscoskiffferry.net</p>
  </section>
</div>
</body>
</html>
```